A4 Single Page Brochure for Private Cloud Offerings

Theme: Futuristic Tech Company

Brightmoor Systems is looking to offer private cloud services for our enterprise customers in Perth-based data-centres that provides our clients with a lower-cost alternative to Nimbra or KLT yielding better performance.

We are looking for a single A4 brochure with a great graphics design theme to promote these services.

We will be providing five tiers:
- Starter
- Growth
- Professional
- Premier
- Elite

Each plan must list on the brochure the Max VMs, CPU cores, Memory and SSD storage allocated. Refer to the uploaded PNG file.

The brochure must list the following selling points:

- Hosted in a local Perth-based TIER3 and TIER4 datacentres
- WA owned hosting - support local
- Low latency - ultra fast local hosting
- Includes Quorra Host Datacentre licensing
- Includes WallHaven Managed Firewalls for Enterprise level threat detection
- Includes all infrastructure maintenance services
- Full self management of VMs through customer portal
- Includes a 1gbps Internet link
- Predictable fixed monthly fee with no dynamic billing
- No additional charges for Storage Transactions, Internet Usage, VM Snapshots, Datacentre Bandwidth Usage and Firewall Traffic Usage.
- Highly available cluster, no single point of failure.
- Pricing is based on 36 months commit
- Yearly rate increases capped to a maximum of Australian CPI
- All plans have 24/7/365 support with dedicated after hours number.
- Managed backup and managed disaster recovery services can be added to plans

Service provided in accordance with our terms and conditions.

We need the ability to EDIT the brochure to adjust pricing after we receive the final project.

Please do not utilise "Pushing the Boundaries of Technology" - our brand is being replaced with "Specialised Consulting". New website is under development but not launched yet.

Target Market(s)

Information Technology Sector

Colors
0054AA
0677BA
7BADD7
CADEEF
E8F1F8

Requirements
Must have
• Theme of Brightmoor is Blue
Should not have
• Extremely stock imagary that just looks "cheap and stock"

```html
<!DOCTYPE html>
<html lang="en">
<head>
<meta charset="utf-8">
<title>Brightmoor Systems – Private Cloud Tiers</title>
<link rel="stylesheet" href="https://fonts.googleapis.com/css2?family=Montserrat:wght@400;500;600;700;800&display=swap">
<style>
:root{
  --brand-blue:#0054AA;
  --brand-mid:#0677BA;
  --brand-sky:#7BADD7;
  --brand-pale:#CADEEF;
  --brand-mist:#E8F1F8;
  --navy:#0a2651;
  --ink:#1d2838;
  --white:#ffffff;
  --charcoal:#1f2023;
}
*{margin:0;padding:0;box-sizing:border-box}
html,body{width:856px;height:1200px;overflow:hidden}
body{font-family:"Montserrat",sans-serif;background:linear-gradient(160deg,#f2f5fa 0%,#e4e9f1 45%,#eef2f8 100%);position:relative;color:var(--ink)}
.hero{position:absolute;left:0;top:0;width:856px;height:288px}
.hero svg{position:absolute;left:0;top:0}
.brand{position:absolute;left:30px;top:42px;display:flex;align-items:center;gap:9px}
.brand-mark{width:24px;height:24px;background:var(--brand-blue)}
.brand-name{font-weight:700;font-size:18px;color:var(--brand-blue);letter-spacing:.4px}
.hero-title{position:absolute;right:27px;top:74px;text-align:right;color:var(--white);font-weight:700;line-height:52px}
.hero-title .line-one{display:block;font-size:50px;margin-right:16px}
.hero-title .line-two{display:block;font-size:52px}
.hero-rule{position:absolute;left:451px;top:191px;width:378px;height:1px;background:var(--white)}
.tagline{position:absolute;right:27px;top:255px;font-size:18px;font-weight:500;color:var(--white);letter-spacing:.2px;white-space:nowrap}
.computer-art{position:absolute;left:30px;top:168px;width:140px;height:118px;border-radius:6px;background:linear-gradient(135deg,#2a6fd0 0%,#15407f 50%,#aeb6c0 100%)}
.tiers-heading{position:absolute;left:0;top:309px;width:856px;height:40px;border-top:1px solid #9aa3b0;border-bottom:1px solid #9aa3b0;background:rgba(255,255,255,.7);text-align:center;font-weight:800;font-size:25.5px;line-height:38px;color:var(--ink);letter-spacing:.3px}
.tier{position:absolute;top:367px;width:151px;height:264px;background:var(--navy);border-radius:24px}
.tier-name{margin:6px 5px 0;height:56px;background:var(--white);border-radius:14px;display:flex;align-items:center;justify-content:center;font-weight:700;font-size:16px;color:var(--ink);letter-spacing:.3px}
.tier-specs{list-style:none;margin:28px 10px 0 6px;color:var(--white);font-size:15px;line-height:22.4px}
.tier-specs li{display:flex;justify-content:space-between}
.services-title{position:absolute;left:52px;top:654px;width:351px;height:47px;background:#bcdcf8;border:1.5px solid #2a3d5c;border-radius:9px;text-align:center;font-weight:800;font-size:29px;line-height:44px;color:var(--brand-blue)}
.services-panel{position:absolute;left:7px;top:709px;width:491px;height:500px;border-radius:50px 50px 0 0;background:linear-gradient(160deg,#1a6fc4 0%,#1f4ea6 45%,#2b2f82 100%)}
.selling-points{list-style:none;position:absolute;left:38px;top:22px;width:452px;color:var(--white);font-size:14px;line-height:19.4px}
.selling-points li{display:flex;gap:9px;margin-bottom:.6px}
.selling-points svg{flex:none;margin-top:6px}
.selling-points span{display:block}
.photo-circuit{position:absolute;left:511px;top:647px;width:318px;height:100px;border-radius:20px;
  background:radial-gradient(ellipse 30% 45% at 40% 70%,rgba(70,170,190,.55),transparent 70%),
             radial-gradient(ellipse 35% 60% at 75% 45%,rgba(120,60,110,.55),transparent 70%),
             linear-gradient(120deg,#0d2a44 0%,#1b4a68 50%,#2a1c36 100%)}
.photo-hardware{position:absolute;left:512px;top:763px;width:311px;height:321px;border-radius:22px;
  background:radial-gradient(ellipse 40% 30% at 25% 20%,rgba(150,70,50,.55),transparent 70%),
             radial-gradient(ellipse 40% 30% at 75% 25%,rgba(60,120,110,.5),transparent 70%),
             radial-gradient(ellipse 35% 30% at 30% 78%,rgba(170,80,110,.45),transparent 70%),
             radial-gradient(ellipse 35% 30% at 75% 75%,rgba(190,120,50,.45),transparent 70%),
             linear-gradient(150deg,#3b2c2c 0%,#22303e 45%,#1a2640 100%)}
.footer-band{position:absolute;left:498px;top:1094px;width:358px;height:99px;background:var(--charcoal)}
</style>
</head>
<body>
<header class="hero">
  <svg width="856" height="288" viewBox="0 0 856 288" aria-hidden="true">
    <defs>
      <linearGradient id="band" x1="0" x2="1">
        <stop offset="0" stop-color="#dfe6ee"/>
        <stop offset=".45" stop-color="#8fb6df"/>
        <stop offset="1" stop-color="#0677BA"/>
      </linearGradient>
    </defs>
    <rect x="0" y="248" width="856" height="39" fill="url(#band)"/>
    <polygon points="0,0 375,0 285,118 0,118" fill="#ffffff"/>
    <polygon points="375,0 410,0 220,248 185,248" fill="#0b5f86"/>
    <polygon points="410,0 455,0 268,248 220,248" fill="#0677BA"/>
    <polygon points="455,0 490,0 305,248 268,248" fill="#0a94c4"/>
    <polygon points="490,0 528,0 343,248 305,248" fill="#1078b8"/>
  </svg>
  <div role="img" aria-label="Photo of a desk with a keyboard in blue light" style="position:absolute;left:0;top:118px;width:200px;height:130px;background:linear-gradient(90deg,#0a3b86,#1553a8)"></div>
  <div role="img" aria-label="Photo of a workstation keyboard and monitor in blue light" style="position:absolute;left:343px;top:0;width:513px;height:248px;clip-path:polygon(185px 0,513px 0,513px 248px,0 248px);background:linear-gradient(135deg,#0b2a66 0%,#123f93 50%,#0a2a68 100%)"></div>
  <div class="brand">
    <span class="brand-mark"></span>
    <span class="brand-name">BRIGHTMOOR SYSTEMS</span>
  </div>
  <h1 class="hero-title"><span class="line-one">Futuristic</span><span class="line-two">Tech Company</span></h1>
  <div class="hero-rule"></div>
  <p class="tagline">Redefining Computing for a Smarter Future</p>
  <div class="computer-art" role="img" aria-label="Illustration of a desktop computer and monitor"></div>
</header>

<h2 class="tiers-heading">WE WILL BE PROVIDING FIVE TIERS</h2>

<section class="tier" style="left:41px">
  <h3 class="tier-name">STARTER</h3>
  <ul class="tier-specs"><li><span>Max VMs</span><span>5</span></li><li><span>CPU cores</span><span>8</span></li><li><span>Memory</span><span>64</span></li><li><span>SSD storage</span><span>3</span></li></ul>
</section>
<section class="tier" style="left:200px">
  <h3 class="tier-name">GROWTH</h3>
  <ul class="tier-specs"><li><span>Max VMs</span><span>10</span></li><li><span>CPU cores</span><span>16</span></li><li><span>Memory</span><span>128</span></li><li><span>SSD storage</span><span>8</span></li></ul>
</section>
<section class="tier" style="left:360px">
  <h3 class="tier-name">PROFESSIONAL</h3>
  <ul class="tier-specs"><li><span>Max VMs</span><span>15</span></li><li><span>CPU cores</span><span>32</span></li><li><span>Memory</span><span>192</span></li><li><span>SSD storage</span><span>15</span></li></ul>
</section>
<section class="tier" style="left:519px">
  <h3 class="tier-name">ELITE</h3>
  <ul class="tier-specs"><li><span>Max VMs</span><span>20</span></li><li><span>CPU cores</span><span>48</span></li><li><span>Memory</span><span>256</span></li><li><span>SSD storage</span><span>20</span></li></ul>
</section>
<section class="tier" style="left:679px">
  <h3 class="tier-name">PREMIER</h3>
  <ul class="tier-specs"><li><span>Max VMs</span><span>25</span></li><li><span>CPU cores</span><span>64</span></li><li><span>Memory</span><span>320</span></li><li><span>SSD storage</span><span>30</span></li></ul>
</section>

<h2 class="services-title">OUR SERVICES</h2>

<section class="services-panel">
  <ul class="selling-points">
    <li><svg width="13" height="13" viewBox="0 0 13 13"><rect x=".75" y="1.75" width="10.5" height="10.5" fill="none" stroke="#fff" stroke-width="1.5"/><path d="M3 7l2.5 2.5L12 1" fill="none" stroke="#fff" stroke-width="1.8"/></svg><span>- Hosted in a local Perth-based TIER3 and TIER4 datacentres</span></li>
    <li><svg width="13" height="13" viewBox="0 0 13 13"><rect x=".75" y="1.75" width="10.5" height="10.5" fill="none" stroke="#fff" stroke-width="1.5"/><path d="M3 7l2.5 2.5L12 1" fill="none" stroke="#fff" stroke-width="1.8"/></svg><span>- WA owned hosting - support local</span></li>
    <li><svg width="13" height="13" viewBox="0 0 13 13"><rect x=".75" y="1.75" width="10.5" height="10.5" fill="none" stroke="#fff" stroke-width="1.5"/><path d="M3 7l2.5 2.5L12 1" fill="none" stroke="#fff" stroke-width="1.8"/></svg><span>- Low latency - ultra fast local hosting</span></li>
    <li><svg width="13" height="13" viewBox="0 0 13 13"><rect x=".75" y="1.75" width="10.5" height="10.5" fill="none" stroke="#fff" stroke-width="1.5"/><path d="M3 7l2.5 2.5L12 1" fill="none" stroke="#fff" stroke-width="1.8"/></svg><span>- Includes Quorra Host Datacentre licensing</span></li>
    <li><svg width="13" height="13" viewBox="0 0 13 13"><rect x=".75" y="1.75" width="10.5" height="10.5" fill="none" stroke="#fff" stroke-width="1.5"/><path d="M3 7l2.5 2.5L12 1" fill="none" stroke="#fff" stroke-width="1.8"/></svg><span>- Includes WallHaven Managed Firewalls for Enterprise level threat detection</span></li>
    <li><svg width="13" height="13" viewBox="0 0 13 13"><rect x=".75" y="1.75" width="10.5" height="10.5" fill="none" stroke="#fff" stroke-width="1.5"/><path d="M3 7l2.5 2.5L12 1" fill="none" stroke="#fff" stroke-width="1.8"/></svg><span>- Includes all infrastructure maintenance services</span></li>
    <li><svg width="13" height="13" viewBox="0 0 13 13"><rect x=".75" y="1.75" width="10.5" height="10.5" fill="none" stroke="#fff" stroke-width="1.5"/><path d="M3 7l2.5 2.5L12 1" fill="none" stroke="#fff" stroke-width="1.8"/></svg><span>- Full self management of VMs through customer portal</span></li>
    <li><svg width="13" height="13" viewBox="0 0 13 13"><rect x=".75" y="1.75" width="10.5" height="10.5" fill="none" stroke="#fff" stroke-width="1.5"/><path d="M3 7l2.5 2.5L12 1" fill="none" stroke="#fff" stroke-width="1.8"/></svg><span>- Includes a 1gbps Internet link</span></li>
    <li><svg width="13" height="13" viewBox="0 0 13 13"><rect x=".75" y="1.75" width="10.5" height="10.5" fill="none" stroke="#fff" stroke-width="1.5"/><path d="M3 7l2.5 2.5L12 1" fill="none" stroke="#fff" stroke-width="1.8"/></svg><span>- Predictable fixed monthly fee with no dynamic billing</span></li>
    <li><svg width="13" height="13" viewBox="0 0 13 13"><rect x=".75" y="1.75" width="10.5" height="10.5" fill="none" stroke="#fff" stroke-width="1.5"/><path d="M3 7l2.5 2.5L12 1" fill="none" stroke="#fff" stroke-width="1.8"/></svg><span>- No additional charges for Storage Transactions, Internet Usage, VM Snapshots, Datacentre Bandwidth Usage and Firewall Traffic Usage.</span></li>
    <li><svg width="13" height="13" viewBox="0 0 13 13"><rect x=".75" y="1.75" width="10.5" height="10.5" fill="none" stroke="#fff" stroke-width="1.5"/><path d="M3 7l2.5 2.5L12 1" fill="none" stroke="#fff" stroke-width="1.8"/></svg><span>- Highly available cluster, no single point of failure.</span></li>
    <li><svg width="13" height="13" viewBox="0 0 13 13"><rect x=".75" y="1.75" width="10.5" height="10.5" fill="none" stroke="#fff" stroke-width="1.5"/><path d="M3 7l2.5 2.5L12 1" fill="none" stroke="#fff" stroke-width="1.8"/></svg><span>- Pricing is based on 36 months commit</span></li>
    <li><svg width="13" height="13" viewBox="0 0 13 13"><rect x=".75" y="1.75" width="10.5" height="10.5" fill="none" stroke="#fff" stroke-width="1.5"/><path d="M3 7l2.5 2.5L12 1" fill="none" stroke="#fff" stroke-width="1.8"/></svg><span>- Yearly rate increases capped to a maximum of Australian CPI</span></li>
    <li><svg width="13" height="13" viewBox="0 0 13 13"><rect x=".75" y="1.75" width="10.5" height="10.5" fill="none" stroke="#fff" stroke-width="1.5"/><path d="M3 7l2.5 2.5L12 1" fill="none" stroke="#fff" stroke-width="1.8"/></svg><span>- All plans have 24/7/365 support with dedicated after hours number.</span></li>
    <li><svg width="13" height="13" viewBox="0 0 13 13"><rect x=".75" y="1.75" width="10.5" height="10.5" fill="none" stroke="#fff" stroke-width="1.5"/><path d="M3 7l2.5 2.5L12 1" fill="none" stroke="#fff" stroke-width="1.8"/></svg><span>- Managed backup and managed disaster recovery services can be added to plans</span></li>
  </ul>
</section>

<div class="photo-circuit" role="img" aria-label="Close-up photo of a circuit board with chips in teal and magenta light"></div>
<div class="photo-hardware" role="img" aria-label="Collage of four photos of computer hardware and graphics cards in warm and cool light"></div>
<div class="footer-band"></div>
</body>
</html>
```